Tallgrove Vale Management

I need a professional website. My current website is tallgrovevalemanagement.com and I hate it. It was created with some AI tool very quickly because I needed a site up and running with no advanced notice. I’m open to all designs .. I trust you, the professionals will deliver the results I’m anxiously awaiting! :)

```html
<!DOCTYPE html>
<html lang="en">
<head>
<meta charset="utf-8">
<title>Tallgrove Vale Management</title>
<link href="https://fonts.googleapis.com/css2?family=Montserrat:wght@600;700;800&family=Open+Sans:wght@400;600&display=swap" rel="stylesheet">
<style>
:root{
  --navy:#13294b;
  --navy-deep:#0f2342;
  --red:#d50c22;
  --ink:#13294b;
  --muted:#6b7486;
  --line:#e3e6ec;
  --soft:#f0f1f4;
  --white:#ffffff;
}
*{box-sizing:border-box;margin:0;padding:0}
html,body{width:1200px;height:3309px;overflow:hidden}
body{font-family:"Open Sans",sans-serif;color:var(--ink);background:var(--white);position:relative}
.wrap{width:770px;margin:0 auto;position:relative}
h1,h2,h3,h4,.brand,.btn,.eyebrow,.nav a{font-family:"Montserrat",sans-serif}
.eyebrow{font-size:9px;font-weight:700;letter-spacing:.6px;color:var(--red);text-transform:uppercase}
h2{font-size:32px;font-weight:800;line-height:38px;color:var(--navy)}
.btn{display:inline-flex;align-items:center;gap:6px;height:31px;padding:0 17px;font-size:9px;font-weight:700;letter-spacing:.4px;text-transform:uppercase;text-decoration:none;color:var(--white);background:var(--red)}
.btn.outline{background:transparent;border:1.5px solid var(--white)}
.btn.navy{background:var(--navy)}
.icon{width:11px;height:11px;fill:none;stroke:currentColor;stroke-width:2}

/* hero */
.hero{height:563px;background:linear-gradient(180deg,#122848 0%,#1b3358 55%,#1d355c 100%);color:var(--white);position:relative}
.topbar{height:55px;display:flex;align-items:center;justify-content:space-between;border-bottom:1px solid rgba(255,255,255,.18)}
.brand{font-size:11px;font-weight:700;color:var(--white);display:flex;align-items:center;gap:6px}
.brand i{width:14px;height:14px;border-radius:50%;background:var(--red);display:block}
.call{font-size:9px;display:flex;align-items:center;gap:6px;color:#dfe5ef}
.call svg{color:var(--red)}
.socials{display:flex;gap:8px}
.socials span{width:11px;height:11px;border-radius:50%;border:1.5px solid var(--red);display:block}
.navrow{height:50px;display:flex;align-items:center;justify-content:space-between}
.nav{display:flex;gap:20px}
.nav a{font-size:9px;font-weight:600;color:var(--white);text-decoration:none}
.nav a.active{color:var(--red)}
.hero-copy{padding-top:100px}
.hero-copy .eyebrow{font-size:11px;letter-spacing:0;text-transform:none}
.hero-copy h1{font-size:45px;font-weight:800;line-height:56px;margin-top:10px}
.hero-copy p{font-size:11.5px;line-height:17.5px;width:410px;margin-top:18px;color:#d7deea}
.hero-btns{display:flex;gap:11px;margin-top:24px}

/* stats */
.stats{position:absolute;top:523px;left:215px;width:770px;height:280px;display:flex;background:var(--white);box-shadow:0 10px 30px rgba(19,41,75,.15);z-index:2}
.stats .lead{width:273px;background:var(--red);color:var(--white);padding:30px 30px}
.stats .lead .eyebrow{color:var(--white)}
.stats .lead h3{font-family:"Montserrat",sans-serif;font-size:22px;line-height:28px;font-weight:800;color:var(--navy);margin-top:8px}
.stats .lead p{font-size:9.5px;line-height:15px;color:#ffc8cd;margin-top:14px}
.stats .lead .btn{margin-top:15px;height:27px;padding:0 15px}
.stat{flex:1;border-left:1px solid var(--line);padding:24px 25px}
.stat b{font-family:"Montserrat",sans-serif;font-size:27px;font-weight:800;color:var(--navy);display:block}
.stat span{font-size:8.5px;color:var(--muted);display:block;margin-top:6px}

/* services */
.services{padding-top:306px;height:907px}
.sec-head{display:flex;justify-content:space-between;align-items:flex-end}
.sec-head h2{margin-top:4px}
.view{font-family:"Montserrat",sans-serif;font-size:8.5px;font-weight:700;color:var(--navy);margin-bottom:6px}
.grid3{display:grid;grid-template-columns:repeat(3,244px);gap:20px 19px;margin-top:18px}
.card{height:225px;background:var(--white);box-shadow:0 4px 14px rgba(19,41,75,.1)}
.ph{display:block;height:140px}
.ph.a{background:linear-gradient(135deg,#3b3630,#7a6d5f 60%,#cfc6b8)}
.ph.b{background:linear-gradient(135deg,#ddd6cc,#8a6a4e 55%,#3c4660)}
.ph.c{background:linear-gradient(135deg,#f1efea,#c9c4ba 50%,#5a8a4a)}
.ph.d{background:linear-gradient(135deg,#4a3b33,#8b5a3c 50%,#2d3850)}
.ph.e{background:linear-gradient(135deg,#c9b89e,#5b5446 55%,#8fa06a)}
.ph.f{background:linear-gradient(135deg,#f3f1ec,#d8d3c8 55%,#6b6f77)}
.card h4{font-size:12px;font-weight:700;color:var(--navy);margin:20px 17px 0}
.card p{font-size:8.5px;line-height:13px;color:var(--muted);margin:8px 17px 0}

/* commitment */
.commit{background:var(--soft);height:476px}
.commit .wrap{display:flex;justify-content:space-between;height:100%;align-items:center}
.commit .photo{width:367px;height:244px;background:linear-gradient(135deg,#e8eae6,#9aa09a 45%,#5d6b57 75%,#e6c84e)}
.commit .text{width:367px}
.commit h2{margin-top:10px}
.commit p{font-size:9.5px;line-height:15px;color:var(--muted);margin-top:14px}
.commit .btn{margin-top:14px;height:27px}
.commit h4{font-size:15px;font-weight:700;color:var(--navy);margin-top:28px}
.commit .small{font-size:8px;line-height:12px;margin-top:8px}
.checks{display:grid;grid-template-columns:1fr 1fr;gap:8px 0;margin-top:12px;list-style:none}
.checks li{font-family:"Montserrat",sans-serif;font-size:8.5px;font-weight:600;color:var(--navy);display:flex;align-items:center;gap:8px}
.checks svg{width:15px;height:15px}

/* communities */
.areas{height:418px;padding-top:66px}
.areas h2{margin-top:6px}
.areas .intro{font-size:9.5px;line-height:15px;color:var(--muted);width:410px;margin-top:18px}
.area-cards{display:grid;grid-template-columns:repeat(3,244px);gap:19px;margin-top:32px}
.area{height:132px;border-left:3px solid var(--red);background:var(--white);box-shadow:0 4px 14px rgba(19,41,75,.08);padding:20px 20px}
.area svg{width:13px;height:14px;color:var(--red)}
.area h4{font-size:12px;font-weight:700;color:var(--navy);margin-top:8px}
.area p{font-size:8.5px;line-height:13px;color:var(--muted);margin-top:6px}
.area a{display:block;font-family:"Montserrat",sans-serif;font-size:8.5px;font-weight:700;color:var(--navy);text-decoration:none;margin-top:8px}

/* portfolio */
.portfolio{background:var(--navy);height:397px;padding-top:63px}
.portfolio h2{color:var(--white);margin-top:4px}
.portfolio .view{color:var(--red)}
.props{display:grid;grid-template-columns:repeat(4,181px);gap:15px;margin-top:24px}
.prop{height:195px;position:relative;color:var(--white)}
.prop.a{background:linear-gradient(180deg,#4d6a3a,#2d3a26 60%,#142036)}
.prop.b{background:linear-gradient(180deg,#9fb8d6,#4a4f5a 55%,#152238)}
.prop.c{background:linear-gradient(180deg,#a9bdd4,#7a5a4c 50%,#152238)}
.prop.d{background:linear-gradient(180deg,#5d7a3e,#8f8f86 55%,#152238)}
.prop h4{position:absolute;left:15px;bottom:22px;font-size:11px;font-weight:700}
.prop span{position:absolute;left:15px;bottom:10px;font-size:8px;color:#c7cfdc}

/* proposal + faq */
.contact{height:455px;padding-top:62px}
.contact .wrap{display:flex;justify-content:space-between}
.form-col,.faq-col{width:367px}
.form-col h2{margin-top:12px}
.form-col p{font-size:9.5px;line-height:15px;color:var(--muted);margin-top:14px}
.form{margin-top:18px;display:grid;grid-template-columns:1fr 1fr;gap:10px 9px}
.field{height:28px;background:var(--soft);border:1px solid var(--line);font-size:8px;color:#9aa1ad;padding:9px 10px}
.field.full{grid-column:1/3}
.field.area-f{height:82px}
.form-col .btn{margin-top:10px;height:29px}
.faq-col h2{margin-top:6px;line-height:32px}
.faq{list-style:none;margin-top:20px}
.faq li{height:45px;border:1px solid var(--line);box-shadow:0 3px 10px rgba(19,41,75,.06);display:flex;align-items:center;justify-content:space-between;padding:0 15px;font-family:"Montserrat",sans-serif;font-size:9px;font-weight:700;color:var(--navy);margin-bottom:11px}
.faq li b{color:var(--red);font-size:11px}

/* footer */
.footer{background:var(--navy);height:93px}
.footer .wrap{height:100%;display:flex;align-items:center;justify-content:space-between}
.footer p{font-size:8.5px;color:#b8c2d2}
</style>
</head>
<body>

<header class="hero">
  <div class="wrap">
    <div class="topbar">
      <div class="brand"><i></i>Tallgrove Vale</div>
      <div class="call"><svg class="icon" viewBox="0 0 24 24"><path d="M5 3h4l2 5-2.5 1.5a11 11 0 0 0 6 6L16 13l5 2v4a2 2 0 0 1-2 2A16 16 0 0 1 3 5a2 2 0 0 1 2-2z"/></svg>Make a call: (216) 555-0187</div>
      <div class="socials"><span></span><span></span><span></span><span></span></div>
    </div>
    <div class="navrow">
      <nav class="nav"><a class="active" href="#">Home</a><a href="#">Projects</a><a href="#">Services</a><a href="#">About</a><a href="#">Contact Us</a></nav>
      <a class="btn" href="#">Get a Proposal</a>
    </div>
    <div class="hero-copy">
      <div class="eyebrow">Cleveland · Akron Property Management</div>
      <h1>A True Partner,<br>Not Just A Vendor.</h1>
      <p>Tallgrove Vale Management applies rigorously tested frameworks and data-driven methodologies to safeguard property value while elevating tenant experience across Northeast Ohio.</p>
      <div class="hero-btns"><a class="btn" href="#">Our Services</a><a class="btn outline" href="#">Contact Us</a></div>
    </div>
  </div>
</header>

<section class="stats">
  <div class="lead">
    <div class="eyebrow">Asset Preservation</div>
    <h3>Expertise Rooted In Long-Term Value</h3>
    <p>Drawing on decades of collective expertise, our team facilitates regulatory compliance, cost efficiency, and proactive maintenance for owners across Ohio.</p>
    <a class="btn navy" href="#">Work With Us <svg class="icon" viewBox="0 0 24 24"><path d="M4 12h15M13 6l6 6-6 6"/></svg></a>
  </div>
  <div class="stat"><b>500+</b><span>Units Under Management</span></div>
  <div class="stat"><b>20+</b><span>Years Serving Ohio</span></div>
  <div class="stat"><b>98%</b><span>Occupancy Retention Rate</span></div>
</section>

<section class="services">
  <div class="wrap">
    <div class="sec-head">
      <div><div class="eyebrow">A True Partner</div><h2>Quality Services</h2></div>
      <span class="view">VIEW ALL →</span>
    </div>
    <div class="grid3">
      <article class="card"><span class="ph a" role="img" aria-label="Two managers reviewing documents in an office"></span><h4>Tenant Relations</h4><p>Consultative screening, onboarding, and communication that keeps occupancy strong.</p></article>
      <article class="card"><span class="ph b" role="img" aria-label="Technician repairing household plumbing"></span><h4>Maintenance &amp; Repairs</h4><p>Proactive, vendor-vetted maintenance that protects asset value around the clock.</p></article>
      <article class="card"><span class="ph c" role="img" aria-label="Laptop showing financial charts on a desk"></span><h4>Financial Reporting</h4><p>Transparent monthly statements and data-driven insights on every property.</p></article>
      <article class="card"><span class="ph d" role="img" aria-label="Handshake across a meeting table"></span><h4>Leasing &amp; Renewals</h4><p>Strategic lease structuring designed to maximize retention and revenue.</p></article>
      <article class="card"><span class="ph e" role="img" aria-label="Inspector with clipboard outside a house"></span><h4>Property Inspections</h4><p>Rigorous inspection frameworks that safeguard condition and compliance.</p></article>
      <article class="card"><span class="ph f" role="img" aria-label="Agent showing a bright living room"></span><h4>Marketing &amp; Placement</h4><p>Targeted marketing that fills vacancies quickly with qualified residents.</p></article>
    </div>
  </div>
</section>

<section class="commit">
  <div class="wrap">
    <div class="photo" role="img" aria-label="Team meeting around a conference table"></div>
    <div class="text">
      <div class="eyebrow">Our Commitment</div>
      <h2>Committed To Preserving Value &amp; Community</h2>
      <p>Our disciplined approach enables owners to preserve capital, enhance occupancy rates, and demonstrate long-term resilience across diverse market conditions.</p>
      <a class="btn" href="#">Get In Touch <svg class="icon" viewBox="0 0 24 24"><path d="M4 12h15M13 6l6 6-6 6"/></svg></a>
      <h4>We Follow Best Practices</h4>
      <p class="small">Every property is managed to the same rigorous standards that protect owners and residents.</p>
      <ul class="checks">
        <li><svg viewBox="0 0 16 16"><circle cx="8" cy="8" r="8" fill="#d50c22"/><path d="M4.5 8.2l2.3 2.2 4.5-4.6" stroke="#fff" stroke-width="1.8" fill="none"/></svg>Asset Preservation</li>
        <li><svg viewBox="0 0 16 16"><circle cx="8" cy="8" r="8" fill="#d50c22"/><path d="M4.5 8.2l2.3 2.2 4.5-4.6" stroke="#fff" stroke-width="1.8" fill="none"/></svg>Regulatory Compliance</li>
        <li><svg viewBox="0 0 16 16"><circle cx="8" cy="8" r="8" fill="#d50c22"/><path d="M4.5 8.2l2.3 2.2 4.5-4.6" stroke="#fff" stroke-width="1.8" fill="none"/></svg>Proactive Maintenance</li>
        <li><svg viewBox="0 0 16 16"><circle cx="8" cy="8" r="8" fill="#d50c22"/><path d="M4.5 8.2l2.3 2.2 4.5-4.6" stroke="#fff" stroke-width="1.8" fill="none"/></svg>Transparent Reporting</li>
      </ul>
    </div>
  </div>
</section>

<section class="areas">
  <div class="wrap">
    <div class="eyebrow">Where We Operate</div>
    <h2>Serving Communities<br>Across Northeast Ohio</h2>
    <p class="intro">From historic Cleveland neighborhoods to growing Akron suburbs, our team is on the ground where your assets live.</p>
    <div class="area-cards">
      <div class="area"><svg viewBox="0 0 24 26" fill="none" stroke="currentColor" stroke-width="2"><path d="M12 24s8-8 8-14a8 8 0 0 0-16 0c0 6 8 14 8 14z"/><circle cx="12" cy="10" r="3"/></svg><h4>Cleveland</h4><p>Serving Brooklyn Centre, Tremont, Ohio City &amp; the West Side</p><a href="#">Contact →</a></div>
      <div class="area"><svg viewBox="0 0 24 26" fill="none" stroke="currentColor" stroke-width="2"><path d="M12 24s8-8 8-14a8 8 0 0 0-16 0c0 6 8 14 8 14z"/><circle cx="12" cy="10" r="3"/></svg><h4>Akron</h4><p>Serving Highland Square, West Akron &amp; greater Summit County</p><a href="#">Contact →</a></div>
      <div class="area"><svg viewBox="0 0 24 26" fill="none" stroke="currentColor" stroke-width="2"><path d="M12 24s8-8 8-14a8 8 0 0 0-16 0c0 6 8 14 8 14z"/><circle cx="12" cy="10" r="3"/></svg><h4>Cuyahoga County</h4><p>Serving Lakewood, Parma &amp; inner-ring suburbs</p><a href="#">Contact →</a></div>
    </div>
  </div>
</section>

<section class="portfolio">
  <div class="wrap">
    <div class="sec-head">
      <div><div class="eyebrow">Portfolio</div><h2>Properties We Manage</h2></div>
      <span class="view">VIEW PROJECTS →</span>
    </div>
    <div class="props">
      <div class="prop a" role="img" aria-label="Tree-lined residential street"><h4>Brooklyn Centre Portfolio</h4><span>Cleveland, OH</span></div>
      <div class="prop b" role="img" aria-label="Brick apartment building"><h4>Downtown Residences</h4><span>Akron, OH</span></div>
      <div class="prop c" role="img" aria-label="Row of multi-family townhomes"><h4>Tremont Multi-Family</h4><span>Cleveland, OH</span></div>
      <div class="prop d" role="img" aria-label="Suburban single-family house"><h4>Suburban Single-Family</h4><span>Cuyahoga County, OH</span></div>
    </div>
  </div>
</section>

<section class="contact">
  <div class="wrap">
    <div class="form-col">
      <h2>Request a Tailored Proposal</h2>
      <p>Ready to work together? Submit the form to initiate a consultative assessment and explore solutions aligned with your objectives.</p>
      <div class="form">
        <div class="field">First Name</div>
        <div class="field">Last Name</div>
        <div class="field full">Email</div>
        <div class="field full area-f">Tell us about your portfolio</div>
      </div>
      <a class="btn" href="#">Send Message</a>
    </div>
    <div class="faq-col">
      <div class="eyebrow">Learn More From Us</div>
      <h2>Frequently Asked Questions</h2>
      <ul class="faq">
        <li>1. What areas do you serve? <b>+</b></li>
        <li>2. How do you protect asset value? <b>+</b></li>
        <li>3. What does your fee structure look like? <b>+</b></li>
      </ul>
    </div>
  </div>
</section>

<footer class="footer">
  <div class="wrap">
    <div class="brand"><i></i>Tallgrove Vale</div>
    <p>© 2026 Tallgrove Vale Management. A true partner, not just a vendor.</p>
    <div class="socials"><span></span><span></span><span></span><span></span></div>
  </div>
</footer>

</body>
</html>
```